Renewable Energy Consultancy needs relatively simple but smart website

We are a renewable energy focussed consultancy called Bellmoran, and we are just starting out. Our target is to bring knowledge of the detailed technical and commercial operations of renewables projects, mainly wind energy.

Our target customers are major energy utilities and private finance groups, who look to invest in renewables projects as a long term money-earning system. We are a fairly young, dynamic team of industry-respected people (4 of us) but we need to make ourselves look bigger than this (our customers will expect us to take on major projects, so we need to look big enough to handle it...)

We're not going to sell anything from our website and we expect it to just support our company name. Most of our customers are made by strong networks and relationships, so its mainly there to give confidence in our capabilities and give a strong view of who we are. We probably need a site with 4/5 pages which we can then expand when needed.

We have logos and headers (attached) which we want to use (also run through artpitchly), and I've attached a few pictures of projects similar to those we will be involved in to give us a feel for how it will look. Also attached are the colours we liked which are now used in the logo, and the font details. Whilst we're a "green" company with a "green" logo, we don't want to be completely green, so some nice combinations of colours on the pages would be good.

Ideally we need to have chirpnet/workgrid news feeds somewhere linked into the site.

The design should be smart - giving a feel of high integrity and assurance whilst making us seem approachable and knowledgeable.

Target Market(s)

Renewables investors, developers of renewables projects (wind farms etc),

Industry/Entity Type

Finance

Coding

Coded - Design and coding required

Number of Pages Required

4 page

Other font styles liked:
• See the attachment with brand text/colour details ("colour codes" filename)

Requirements
Must have
• A fairly simple, but smart website design. We're looking to provide confidence and consolidate our networks with the website, not specifically find new customers - so its really just to give customers somewhere they can relate to online
Nice to have
• We have logos/brands and colours - so a website which incorperates these well and brings accross a professional company
• Would be nice to have a page (such as a blog/wordpress) we can easily update with news/events etc and links to chirpnet feed and workgrid feed ideally.
Should not have
• cartoons, flashy gimmicks,

```html
<!DOCTYPE html>
<html lang="en">
<head>
<meta charset="utf-8">
<title>Bellmoran — Renewable Energy Consultancy</title>
<link rel="stylesheet" href="https://fonts.googleapis.com/css2?family=Dosis:wght@300;400;500;600&family=Noto+Serif&family=Open+Sans:wght@400&display=swap">
<style>
:root{
  --green:#6aa818;
  --green-soft:#8cc43a;
  --green-dark:#2f5c08;
  --heading:#2e5a07;
  --text:#555;
  --muted:#999;
  --field:#f1f1f1;
  --band:#fafafa;
  --line:#e6e6e6;
  --white:#fff;
}
*{box-sizing:border-box;margin:0;padding:0}
html,body{width:1200px;height:2829px;overflow:hidden}
body{position:relative;background:var(--white);font-family:"Open Sans",Arial,sans-serif;color:var(--text)}
.abs{position:absolute}

/* header */
.site-header{left:0;top:0;width:1200px;height:88px;background:var(--white);border-bottom:1px solid var(--line)}
.brand{left:172px;top:14px;display:flex;align-items:center;gap:14px}
.brand-dot{width:56px;height:56px;border-radius:50%;background:var(--green)}
.brand-name{font-family:"Dosis",sans-serif;font-weight:300;font-size:50px;color:#444;letter-spacing:1px}
.nav{left:578px;top:24px;display:flex;gap:0;font-family:"Dosis",sans-serif;font-size:17px;color:#555}
.nav a{display:block;padding:8px 13px;color:inherit;text-decoration:none;text-transform:uppercase}
.nav a.active{color:var(--green);border:2px solid var(--green-soft);padding:6px 22px;margin-right:6px}

/* hero */
.hero{left:0;top:88px;width:1200px;height:622px;background:linear-gradient(180deg,#7fb52a 0%,#6ea61c 55%,#5f9612 100%)}
.hero-brand{left:0;top:148px;width:1200px;display:flex;justify-content:center;align-items:center;gap:18px}
.hero-brand .brand-dot{width:70px;height:70px;background:rgba(255,255,255,.9)}
.hero-brand .brand-name{color:var(--white);font-size:60px}
.hero-text{left:230px;top:258px;width:740px;text-align:center;color:var(--white);font-family:"Dosis",sans-serif;font-size:22px;line-height:36px}
.hero-buttons{left:0;top:400px;width:1200px;display:flex;justify-content:center;gap:20px}
.hero-btn{display:flex;align-items:center;gap:12px;height:52px;padding:0 28px;background:#eaf2dc;border:4px solid rgba(255,255,255,.45);outline:1px solid rgba(255,255,255,.7);font-family:"Dosis",sans-serif;font-size:14px;color:#333;text-transform:uppercase}
.hero-btn i{width:12px;height:12px;background:var(--green)}

/* what we do */
.what-title{left:240px;top:812px;width:420px;text-align:center;font-family:"Dosis",sans-serif;font-weight:500;font-size:40px;color:var(--heading)}
.what-text{left:245px;top:880px;width:410px;text-align:center;font-family:"Noto Serif",Georgia,serif;font-size:16px;line-height:29px;color:#333}
.what-mark{left:685px;top:800px;width:300px;height:280px}

/* who we work with */
.partners{left:0;top:1122px;width:1200px;height:610px;background:var(--band);border-top:1px solid var(--line);border-bottom:1px solid var(--line)}
.section-title{left:0;width:1200px;text-align:center;font-family:"Dosis",sans-serif;font-weight:500;font-size:36px;color:var(--heading)}
.service{left:172px;width:352px}
.service h3{font-family:"Dosis",sans-serif;font-weight:500;font-size:24px;letter-spacing:4px;color:var(--heading);padding-bottom:10px;border-bottom:1px solid var(--line)}
.service p{margin-top:10px;font-size:11px;line-height:18px;color:#888}
.photo{border-radius:50% 50% 14px 14px / 42% 42% 14px 14px}
.photo-a{left:562px;top:1283px;width:250px;height:280px;background:linear-gradient(160deg,#5a8fc4,#d9a06a 70%,#a06a40)}
.photo-b{left:773px;top:1205px;width:225px;height:228px;background:linear-gradient(170deg,#c8d3dc,#6f7780 60%,#8d2a22)}
.photo-c{left:705px;top:1402px;width:283px;height:298px;background:linear-gradient(180deg,#4f7fd0,#8fb3e6 55%,#1a2430 90%)}

/* testimonial */
.avatar{left:240px;top:1790px;width:100px;height:100px;border-radius:50%;background:radial-gradient(circle,#e9c79a,#d8a86c 60%,#f4e8d0 62%)}
.avatar-name{left:240px;top:1895px;width:100px;text-align:center;font-size:11px;color:var(--muted)}
.quote-mark{font-family:"Noto Serif",serif;font-size:34px;color:#888}
.quote{left:395px;top:1796px;width:560px;font-family:"Dosis",sans-serif;font-size:25px;line-height:38px;color:#8a8a8a}
.quote-role{left:395px;top:1895px;font-size:11px;color:var(--muted)}
.dots{left:588px;top:1932px;display:flex;gap:10px}
.dots span{width:7px;height:7px;border-radius:50%;background:#ddd}
.dots span.on{background:#555}

/* clients */
.clients-band{left:0;top:1977px;width:1200px;height:350px;background:var(--band)}
.client-row{left:172px;top:2104px;width:880px;display:flex;justify-content:space-between;align-items:center;font-family:"Dosis",sans-serif;font-weight:600;font-size:22px;color:#777}
.client-row span{display:flex;align-items:center;gap:6px}
.client-row i{width:14px;height:14px;border-radius:50%;background:#888}
.cta{left:487px;top:2176px;width:240px;height:50px;background:var(--green-dark);color:var(--white);font-family:"Dosis",sans-serif;font-size:16px;display:flex;align-items:center;justify-content:center;text-transform:uppercase;border:2px solid #1f4004}

/* contact */
.block-title{font-family:"Dosis",sans-serif;font-weight:500;font-size:27px;color:var(--heading)}
.block-sub{font-size:10px;color:#888;margin-top:6px}
.field{background:var(--field);font-family:"Dosis",sans-serif;font-size:12px;color:#666;padding:12px 18px;text-transform:uppercase}
.send{background:var(--green);color:var(--white);font-family:"Dosis",sans-serif;font-size:18px;display:flex;align-items:center;justify-content:center;text-transform:uppercase}
.contact-line{left:760px;display:flex;align-items:center;gap:22px;font-family:"Dosis",sans-serif;font-size:30px;color:#333}
.contact-line.small{font-size:24px}
.landscape{left:0;top:2600px;width:1200px;height:145px;background:linear-gradient(180deg,rgba(106,168,24,0) 0%,rgba(106,168,24,.25) 100%)}

/* footer */
.site-footer{left:0;top:2745px;width:1200px;height:84px;background:linear-gradient(90deg,#2b5c05,#3d7a0c 50%,#2b5c05)}
.copyright{left:172px;top:30px;font-size:12px;color:var(--white)}
.footer-icons{left:885px;top:30px;display:flex;gap:44px;align-items:center}
.footer-icons i{width:12px;height:12px;border-radius:50%;background:rgba(255,255,255,.6)}
</style>
</head>
<body>

<header class="site-header abs">
  <div class="brand abs"><span class="brand-dot"></span><span class="brand-name">Bellmoran</span></div>
  <nav class="nav abs">
    <a class="active" href="#">Home</a><a href="#">Services</a><a href="#">Developers</a><a href="#">Clients</a><a href="#">Contact</a>
  </nav>
</header>

<section class="hero abs" role="img" aria-label="Photograph of wind turbines on green hills under a green-tinted sky"></section>
<div class="hero-brand abs"><span class="brand-dot"></span><span class="brand-name">Bellmoran</span></div>
<p class="hero-text abs">We are a renewable energy focussed consultancy called Bellmoran, and we are just starting out. Our target is to bring knowledge of the detailed technical and commercial operations of renewables projects, mainly wind energy.</p>
<div class="hero-buttons abs">
  <a class="hero-btn"><i></i>Workgrid</a>
  <a class="hero-btn"><i></i>Chirpnet</a>
</div>

<h2 class="what-title abs">WHAT WE DO</h2>
<p class="what-text abs">We are a renewable energy focussed consultancy called Bellmoran, and we are just starting out. Our target is to bring knowledge of the detailed technical and commercial operations of renewables projects, mainly wind energy.</p>
<svg class="what-mark abs" viewBox="0 0 300 280" role="img" aria-label="Bellmoran brand mark">
  <circle cx="140" cy="150" r="128" fill="#4f8d12"/>
  <text x="140" y="160" text-anchor="middle" font-family="Dosis, sans-serif" font-weight="300" font-size="34" fill="#fff">Bellmoran</text>
</svg>

<section class="partners abs"></section>
<h2 class="section-title abs" style="top:1158px">WHOM WE WORK WITH</h2>
<div class="service abs" style="top:1232px"><h3>WIND FARMS</h3><p>We review turbine performance, grid links and site data to help owners plan sound, long term returns on each wind farm.</p></div>
<div class="service abs" style="top:1375px"><h3>DEVELOPERS</h3><p>From early feasibility to financial close, we guide developers through technical checks, contracts and the commercial steps of each project.</p></div>
<div class="service abs" style="top:1518px"><h3>OPERATORS</h3><p>We support operators with clear reporting, availability reviews and maintenance planning that keep turbines running and revenue steady year on year.</p></div>
<div class="photo photo-b abs" role="img" aria-label="Photograph of an offshore installation vessel and crane"></div>
<div class="photo photo-a abs" role="img" aria-label="Photograph of wind turbines at sunset"></div>
<div class="photo photo-c abs" role="img" aria-label="Photograph of two engineers silhouetted beside turbines against a blue sky"></div>

<div class="avatar abs" role="img" aria-label="Portrait photograph of the client"></div>
<div class="avatar-name abs">Mrs Elna</div>
<span class="quote-mark abs" style="left:352px;top:1785px">&ldquo;</span>
<p class="quote abs">Lorem ipsum dolor sit amet, consectetuer adipiscing elit, di nonummy nibh euismod tincidunt ut laoreet.</p>
<span class="quote-mark abs" style="left:875px;top:1848px">&rdquo;</span>
<span class="quote-role abs">CLIENT</span>
<div class="dots abs"><span class="on"></span><span></span><span></span></div>

<section class="clients-band abs"></section>
<h2 class="section-title abs" style="top:2008px">OUR CLIENTS</h2>
<div class="client-row abs">
  <span>Kestrel Daily</span><span>BRW</span><span>Fenlow</span><span><i></i>Quillpost</span><span>Harbourly</span><span>TOVA</span>
</div>
<a class="cta abs">Offshore Project Portfolio</a>

<div class="landscape abs" role="img" aria-label="Silhouettes of wind turbines on grassy ground"></div>

<div class="abs" style="left:177px;top:2322px">
  <h3 class="block-title">CONTACT US NOW !</h3>
  <p class="block-sub">Write what you think about us!</p>
</div>
<div class="field abs" style="left:177px;top:2385px;width:250px;height:44px">Name</div>
<div class="field abs" style="left:433px;top:2385px;width:252px;height:44px">Email</div>
<div class="field abs" style="left:177px;top:2436px;width:508px;height:44px">Phone</div>
<div class="field abs" style="left:177px;top:2487px;width:508px;height:88px">Message</div>
<div class="send abs" style="left:177px;top:2583px;width:508px;height:45px">Send</div>

<div class="abs" style="left:758px;top:2322px">
  <h3 class="block-title">NEWSLETTER SIGNUP</h3>
  <p class="block-sub">Get updated about app, news and updates</p>
</div>
<div class="field abs" style="left:758px;top:2390px;width:270px;height:46px">Email</div>
<div class="send abs" style="left:758px;top:2443px;width:270px;height:45px">Send</div>

<div class="contact-line abs" style="top:2515px">
  <svg width="46" height="46" viewBox="0 0 24 24" fill="none" stroke="#2e5a07" stroke-width="1.6"><path d="M5 3h4l2 5-2.5 1.5a11 11 0 0 0 6 6L16 13l5 2v4a2 2 0 0 1-2 2A16 16 0 0 1 3 5a2 2 0 0 1 2-2z"/></svg>
  <span>(120) 48 62 90</span>
</div>
<div class="contact-line small abs" style="top:2580px">
  <svg width="46" height="40" viewBox="0 0 24 20" fill="none" stroke="#2e5a07" stroke-width="1.6"><rect x="2" y="3" width="20" height="14"/><path d="M2 3l10 8 10-8"/></svg>
  <span>info@greenvane.com</span>
</div>

<footer class="site-footer abs">
  <p class="copyright abs">Copyrights &copy;Bellmoran. All Rights Reserved 2015.</p>
  <div class="footer-icons abs">
    <svg width="14" height="20" viewBox="0 0 14 20" fill="none" stroke="rgba(255,255,255,.7)" stroke-width="1.5"><rect x="1" y="1" width="12" height="18" rx="2"/></svg>
    <i></i><i></i>
  </div>
</footer>

</body>
</html>
```